Business card por a urban DJ, up scale audience target

Need a sober design, modern, conservative colors but i can consider some options, y play rnb, hip hop, EDM and top40.

Business card for contact and personal info, double sided, use logo attrached please; im 42 so i need a card acording to my age an target audience.

Target Market(s)

Adult people, up scale audience

Industry/Entity Type

Music Download

Contact Information for Business Card

Cel (318) 5024471963 www.kelvarodun.com

Requirements
Must have
• open mind
Nice to have
• open mind
Should not have
• DJ

```html
<!DOCTYPE html>
<html lang="en">
<head>
<meta charset="utf-8">
<title>Kelvar – Business Cards</title>
<link rel="stylesheet" href="https://fonts.googleapis.com/css2?family=Michroma&family=Jura:wght@500;600&display=swap">
<style>
  :root {
    --stage: #d6d4e6;
    --card-dark: #2b2b2b;
    --ink-light: #ececec;
    --ink-dark: #2a2a2a;
    --photo-light: #e2e2e2;
    --photo-mid: #9a9a9a;
    --photo-deep: #2e2e2e;
    --shadow: rgba(40, 36, 70, 0.28);
  }
  * { box-sizing: border-box; margin: 0; padding: 0; }
  html, body { width: 1200px; height: 800px; overflow: hidden; }
  body {
    background: var(--stage);
    position: relative;
    font-family: "Jura", sans-serif;
  }
  .card {
    position: absolute;
    width: 450px;
    height: 256px;
    overflow: hidden;
    box-shadow: 0 6px 14px var(--shadow);
  }

  /* Front */
  .card-front {
    left: 515px;
    top: 128px;
    background: var(--card-dark);
    color: var(--ink-light);
    display: flex;
    flex-direction: column;
    align-items: center;
    justify-content: center;
    gap: 18px;
  }
  .brand-name {
    font-family: "Michroma", sans-serif;
    font-size: 50px;
    letter-spacing: 4px;
    line-height: 1;
  }
  .genre-line {
    font-family: "Michroma", sans-serif;
    font-size: 14px;
    letter-spacing: 2px;
    word-spacing: 8px;
  }

  /* Back */
  .card-back {
    left: 225px;
    top: 440px;
  }
  .crowd-photo {
    position: absolute;
    inset: 0;
    background:
      radial-gradient(ellipse at 62% 18%, #f4f4f4 0%, rgba(240,240,240,0) 45%),
      linear-gradient(180deg, var(--photo-mid) 0%, var(--photo-light) 32%, var(--photo-mid) 55%, var(--photo-deep) 78%, #1f1f1f 100%);
  }
  .back-content {
    position: relative;
    height: 100%;
    display: flex;
    flex-direction: column;
    align-items: center;
    padding-top: 42px;
    color: var(--ink-dark);
  }
  .back-content .brand-name {
    font-size: 34px;
    letter-spacing: 3px;
  }
  .rule {
    width: 150px;
    height: 1px;
    background: var(--ink-dark);
    margin: 12px 0 8px;
  }
  .back-content .genre-line {
    font-size: 11px;
    word-spacing: 6px;
  }
  .contact-list {
    list-style: none;
    position: absolute;
    left: 138px;
    top: 168px;
    color: var(--ink-light);
    font-size: 17px;
    font-weight: 600;
    letter-spacing: 1.5px;
  }
  .contact-list li {
    display: flex;
    align-items: center;
    gap: 8px;
    margin-bottom: 8px;
  }
  .contact-icon { width: 14px; height: 14px; flex: none; }
</style>
</head>
<body>

<section class="card card-front">
  <div class="brand-name">KELVAR</div>
  <div class="genre-line">RNB HIPHOP EDM</div>
</section>

<section class="card card-back">
  <div class="crowd-photo" role="img" aria-label="Black and white concert crowd with raised hands under stage lights"></div>
  <div class="back-content">
    <div class="brand-name">KELVAR</div>
    <div class="rule"></div>
    <div class="genre-line">RNB HIPHOP EDM</div>
  </div>
  <ul class="contact-list">
    <li>
      <svg class="contact-icon" viewBox="0 0 14 14" aria-hidden="true">
        <rect x="3.5" y="0.8" width="7" height="12.4" rx="1.3" fill="none" stroke="currentColor" stroke-width="1.3"/>
        <line x1="6" y1="11" x2="8" y2="11" stroke="currentColor" stroke-width="1.2"/>
      </svg>
      <span>(318) 5024471963</span>
    </li>
    <li>
      <svg class="contact-icon" viewBox="0 0 14 14" aria-hidden="true">
        <circle cx="7" cy="7" r="6.2" fill="none" stroke="currentColor" stroke-width="1.3"/>
        <ellipse cx="7" cy="7" rx="2.6" ry="6.2" fill="none" stroke="currentColor" stroke-width="1"/>
        <line x1="0.8" y1="7" x2="13.2" y2="7" stroke="currentColor" stroke-width="1"/>
      </svg>
      <span>www.kelvarodun.com</span>
    </li>
  </ul>
</section>

</body>
</html>
```